Oak Bend Diesel & Trailer Repair needs a logo and business cards*

We need a logo design and cards for a new business in Fernmoor, Pv called Oak Bend Diesel & Trailer Repair. I would like a design with a Hallorway or Drummoke Semi on it and a gray background card with maybe red and white writing. Address is 517 Marsh Hollow Road Fernmoor, Pv 31884 phone is 229-555-0147 Wesley Hardcastle 229-555-0182, Danny Whitlow 229-555-0163 email address oakbenddieselandtrailer@mailexample.net offic enumber is 229-555-0147

Target Market(s)

people needing truck repairs

Logo Text

Oak Bnd Diesel & Trailer Repair

Logo styles of interest
Wordmark Logo
Font styles to use
Serif
Sans Serif

Colors

Designer to choose colors to be used in the design.

Requirements
Must have
• names, address, phone number, email address and a picture of a Hallorway or Drummoke Semi
• i attached a picture of a card that I would like a card similar to
Nice to have
• i would like it it double sided- on the back i want
• We specialize in DOT inspections, Preventative maintenance, Brake repair, Clutch repair, tire repair, on and off site diagnostics, service calls
• Trailer repair

```html
<!DOCTYPE html>
<html lang="en">
<head>
<meta charset="utf-8">
<title>Oak Bend Diesel &amp; Trailer Repair – Business Card</title>
<link rel="stylesheet" href="https://fonts.googleapis.com/css2?family=Della+Respira&display=swap">
<style>
  :root {
    --page: #ffffff;
    --card: #333333;
    --ink: #f4f4f4;
    --accent: #e3141c;
    --truck-tone: #e9e9e9;
    --text-font: "Della Respira", serif;
  }
  html, body {
    margin: 0;
    padding: 0;
    width: 1200px;
    height: 685px;
    overflow: hidden;
    background: var(--page);
  }
  .card {
    position: relative;
    width: 1200px;
    height: 685px;
    background: var(--card);
    border-radius: 53px;
    overflow: hidden;
    font-family: var(--text-font);
    color: var(--ink);
  }
  .wordmark {
    position: absolute;
    left: 84px;
    top: 58px;
    margin: 0;
    font-family: var(--text-font);
    font-weight: 400;
    font-size: 58px;
    line-height: 64px;
    letter-spacing: 3px;
    text-transform: uppercase;
    color: var(--accent);
  }
  .wordmark .line-two {
    display: block;
    padding-left: 128px;
  }
  .truck-art {
    position: absolute;
    left: 86px;
    top: 278px;
    width: 437px;
    height: 336px;
    background: linear-gradient(160deg, #f2f2f2 0%, var(--truck-tone) 60%, #d6d6d6 100%);
    border-radius: 10px;
  }
  .contact {
    position: absolute;
    right: 85px;
    text-align: right;
    margin: 0;
    white-space: nowrap;
  }
  .owners-label { top: 198px; font-size: 46px; }
  .owner { font-size: 30px; }
  .owner-1 { top: 271px; }
  .owner-2 { top: 321px; }
  .address { top: 384px; font-size: 36px; line-height: 54px; }
  .divider {
    position: absolute;
    left: 542px;
    top: 521px;
    width: 573px;
    height: 4px;
    background: var(--ink);
  }
  .web { font-size: 24px; line-height: 38px; top: 546px; }
</style>
</head>
<body>
  <div class="card">
    <h1 class="wordmark">Oak Bend Diesel<span class="line-two">&amp; Trailer Repair</span></h1>

    <div class="truck-art" role="img" aria-label="Illustration of a white semi truck cab, front three-quarter view"></div>

    <p class="contact owners-label">Owners</p>
    <p class="contact owner owner-1">Wesley Hardcastle 229-555-0182</p>
    <p class="contact owner owner-2">Danny Whitlow 229-555-0163</p>
    <p class="contact address">517 Marsh Hollow Road<br>Fernmoor, Pv 31884</p>

    <div class="divider"></div>

    <p class="contact web">Email : oakbenddieselandtrailer@mailexample.net<br>Fax : 229-555-0147</p>
  </div>
</body>
</html>
```